Corporate Christmas Hamper Guide 2021

We are an online Hamper business in Australia and we need to design and produce our Christmas Hamper brochure for this year. It will need to be a pdf format which will become a digital online brochure. Our business Willowbay Baskets (www.willowbaybaskets.com.au) is a website that curates, packages and delivers hampers for both consumers and corporates. This specific brochure is targetted to the business market. The person who will review the brochure will generally be Executive assistants, Personal Assistants, Marketing Directors and their staff, Senior Managers as well as small business owners. Primaily they will be women.

Hampers are a luxury gift and Christmas is a traditional time for businesses to give their staff, clients, special customers and suppliers a gift to say thankyou for their support over the year. With Covid, this year has made it more difficult to stay connected to colleagues and clients and a hamper is a great way to do that so we anticipate it will be very popular this year.

I have attached our brochure from last year which was a super quick job (not done by a designer). We had recently purchased the business and we just needed to get something out. This is very substandard but I send it to you to see the sorts of things we will include in the brochure.

This job entails intial design and layout then once agreed final production including free image sourcing (hamper photography will be provided but other stylistic and suitable lifestyle photography to enhance the brochure will need to be sourced by you....royalty free). a more detailed design brief is attached below.

```html
<!DOCTYPE html>
<html lang="en">
<head>
<meta charset="utf-8">
<title>Willowbay Baskets – Corporate Christmas Hamper Guide 2021</title>
<link href="https://fonts.googleapis.com/css2?family=Bebas+Neue&family=Nunito+Sans:wght@400;700;800&display=swap" rel="stylesheet">
<style>
:root{
  --backdrop:#8e8e8e;
  --paper:#ffffff;
  --red:#c8202a;
  --red-dark:#a51c22;
  --ink:#1d1d1d;
  --text:#3a3a3a;
  --footer:#262424;
  --icon:#e08a2c;
  --panel:#efefef;
}
*{box-sizing:border-box;margin:0;padding:0}
html,body{width:861px;height:1200px;overflow:hidden;background:var(--backdrop)}
body{position:relative;font-family:"Nunito Sans",Arial,sans-serif;color:var(--text)}
.page{position:absolute;width:393px;height:556px;background:var(--paper);overflow:hidden}
.page--cover{left:27px;top:31px}
.page--intro{left:444px;top:31px}
.page--under100{left:27px;top:609px}
.page--under120{left:444px;top:609px}

.brand{position:absolute;left:0;right:0;top:26px;text-align:center;font-weight:800;color:var(--ink);font-size:26px;line-height:23px;letter-spacing:-.5px}

.cover-band{position:absolute;left:0;top:87px;width:100%;height:81px;background:linear-gradient(90deg,var(--red-dark),var(--red));color:#fff;font-family:"Bebas Neue",Impact,sans-serif;font-size:31px;line-height:33px;text-align:center;padding-top:8px;letter-spacing:.5px}
.cover-photo{position:absolute;left:0;top:168px;width:100%;height:358px;background:radial-gradient(ellipse at 55% 60%,#d98a52 0%,#b8643a 35%,#6e3d24 75%,#4a2a1a 100%)}

.intro-photo{position:absolute;left:0;top:0;width:100%;height:526px;background:linear-gradient(180deg,#fff 0%,#fff 52%,#e3ebf2 68%,#cbd8e4 80%,#c64048 88%,#e9eef3 96%,#fff 100%)}
.intro-panel{position:absolute;left:33px;top:84px;width:328px;height:239px;background:var(--panel);text-align:center;font-size:8.4px;line-height:11.1px;color:#222;padding:13px 8px 0}
.intro-panel p{margin-bottom:11px}
.intro-panel .note{font-size:7px;margin-top:-1px}
.early-bird{position:absolute;left:30px;right:30px;top:334px;text-align:center;color:#222;font-size:8.4px;line-height:11.1px}
.early-bird h2{font-size:11.5px;font-weight:800;margin-bottom:4px}

.footer{position:absolute;left:0;bottom:0;width:100%;height:30px;background:var(--footer);display:flex;align-items:center;justify-content:center;gap:9px;color:#fff;font-size:8.3px}
.footer span{display:flex;align-items:center;gap:3px}
.footer svg{width:13px;height:13px}

.section-band{position:absolute;left:0;top:18px;width:100%;height:23px;background:linear-gradient(90deg,var(--red-dark),var(--red));color:#fff;text-align:center;font-weight:800;font-size:14px;line-height:23px}

.item{position:absolute;width:169px;font-size:8.4px;line-height:11.1px;text-align:justify}
.item-title{color:var(--red);font-weight:800;font-size:10.5px;line-height:12px;margin-bottom:9px;display:flex;justify-content:space-between;align-items:flex-start}
.price{background:var(--red);color:#fff;font-weight:400;font-size:13.5px;line-height:16px;padding:0 4px;white-space:nowrap}
.photo{position:absolute;width:168px;overflow:hidden}
.ribbon{position:absolute;top:0;right:0;width:52px;height:52px}
.ribbon--left{left:0;right:auto}

.wine-list{list-style:none;margin:6px 0 9px}
.wine-list li{display:flex;font-size:8.4px;line-height:11.9px;text-align:left}
.wine-list .dots{flex:1;border-bottom:1px dotted #555;margin:0 2px 3px}
.choose{font-weight:800;color:#222;font-size:8.6px}
</style>
</head>
<body>

<svg width="0" height="0" style="position:absolute">
  <defs>
    <symbol id="icon-phone" viewBox="0 0 16 16"><circle cx="8" cy="8" r="7" fill="none" stroke="#fff" stroke-width="1"/><circle cx="8" cy="8" r="5.3" fill="#e08a2c"/><path d="M6 5.3c.4-.3.8-.2 1 .2l.4.8c.1.3 0 .5-.2.7l-.3.3c.3.7.8 1.2 1.5 1.5l.3-.3c.2-.2.5-.3.7-.2l.8.4c.4.2.5.6.2 1-.6.8-1.7.7-2.7 0S5.8 8.3 5.6 7.3c-.2-.8 0-1.6.4-2z" fill="#fff"/></symbol>
    <symbol id="icon-mail" viewBox="0 0 16 16"><circle cx="8" cy="8" r="7" fill="none" stroke="#fff" stroke-width="1"/><circle cx="8" cy="8" r="5.3" fill="#e08a2c"/><rect x="5" y="6" width="6" height="4.2" fill="#fff"/><path d="M5 6l3 2.3L11 6" fill="none" stroke="#e08a2c" stroke-width=".7"/></symbol>
    <symbol id="icon-web" viewBox="0 0 16 16"><circle cx="8" cy="8" r="7" fill="none" stroke="#fff" stroke-width="1"/><circle cx="8" cy="8" r="5.3" fill="#e08a2c"/><circle cx="8" cy="8" r="3" fill="none" stroke="#fff" stroke-width=".7"/><path d="M5 8h6M8 5c-1.4 1.6-1.4 4.4 0 6M8 5c1.4 1.6 1.4 4.4 0 6" fill="none" stroke="#fff" stroke-width=".6"/></symbol>
    <symbol id="ribbon-right" viewBox="0 0 52 52"><path d="M14 0h16l22 22v16z" fill="#c8202a"/><text x="33" y="18" transform="rotate(45 33 18)" font-family="Nunito Sans, sans-serif" font-size="5.4" font-weight="800" fill="#fff" text-anchor="middle">FREE</text><text x="30" y="24" transform="rotate(45 30 24)" font-family="Nunito Sans, sans-serif" font-size="5.4" font-weight="800" fill="#fff" text-anchor="middle">DELIVERY</text></symbol>
    <symbol id="ribbon-left" viewBox="0 0 52 52"><path d="M38 0H22L0 22v16z" fill="#c8202a"/><text x="19" y="18" transform="rotate(-45 19 18)" font-family="Nunito Sans, sans-serif" font-size="5.4" font-weight="800" fill="#fff" text-anchor="middle">FREE</text><text x="22" y="24" transform="rotate(-45 22 24)" font-family="Nunito Sans, sans-serif" font-size="5.4" font-weight="800" fill="#fff" text-anchor="middle">DELIVERY</text></symbol>
  </defs>
</svg>

<!-- Cover -->
<section class="page page--cover">
  <div class="brand">Willowbay<br>Baskets.</div>
  <h1 class="cover-band">Corporate Christmas<br>Hamper Guide 2021</h1>
  <div class="cover-photo" role="img" aria-label="Stack of kraft-wrapped gifts with red ribbons arranged as a Christmas tree on a rustic wooden backdrop"></div>
  <footer class="footer">
    <span><svg><use href="#icon-phone"/></svg>1300 42 17 88</span>
    <span><svg><use href="#icon-mail"/></svg>corporate@willowbaymail.com</span>
    <span><svg><use href="#icon-web"/></svg>www.willowbaybaskets.com.au</span>
  </footer>
</section>

<!-- Intro -->
<section class="page page--intro">
  <div class="intro-photo" role="img" aria-label="Snowy winter scene with red and silver Christmas baubles along the bottom"></div>
  <div class="brand">Willowbay<br>Baskets.</div>
  <div class="intro-panel">
    <p>Show your clients how much you appreciate them this Christmas! And what better way to express your gratitude than by sending them a beautiful handpacked hamper from the team at Willowbay Baskets.</p>
    <p>We will deliver your corporate gifts anywhere around Australia with FREE Standard Shipping. Or for an additional cost of just $9.95 per hamper there is the Premium service of<br>1 - 2 Business Day delivery.</p>
    <p>Why not tailor your gifts with a free gift card and customised ribbon with your business logo, for maximum brand impact.</p>
    <p>Quality assured, handpicked and taste-tested by our friends, family and staff; the artisan, luxury and award-winning brands we house here at Willowbay Baskets are a genuine pleasure to share.</p>
    <p class="note">*Some hamper items may be substituted due to stock availability at this busy time.</p>
  </div>
  <div class="early-bird">
    <h2>Early Bird Special</h2>
    <p>Receive 5% OFF when you order 10 or more hampers and pay by 13 November. Simply complete our Bulk Order Form and email to corporate@willowbaymail.com and we will apply the discount to your final invoice.*Discount does not apply to shipping*</p>
  </div>
  <footer class="footer">
    <span><svg><use href="#icon-phone"/></svg>1300 42 17 88</span>
    <span><svg><use href="#icon-mail"/></svg>corporate@willowbaymail.com</span>
    <span><svg><use href="#icon-web"/></svg>www.willowbaybaskets.com.au</span>
  </footer>
</section>

<!-- Under $100 -->
<section class="page page--under100">
  <h2 class="section-band">UNDER $100</h2>

  <article class="item" style="left:18px;top:54px">
    <h3 class="item-title">Tempting Treats <span class="price">$75</span></h3>
    <p>Here's a bit of all things tempting! This corporate best seller is packed full of goodies for its lucky recipients. Includes our mouth-watering Pretzels, Beer Nuts, Shortbread Bites, Crackerthins, Soft Jubes, Choc fruit and nuts and Crispy Chocolate Coconut Rolls.</p>
  </article>
  <div class="photo" style="left:206px;top:51px;height:114px;background:linear-gradient(160deg,#fafafa,#ececec 60%,#e2d6c8)" role="img" aria-label="White gift box filled with snacks and sweets">
    <svg class="ribbon"><use href="#ribbon-right"/></svg>
  </div>

  <div class="photo" style="left:19px;top:186px;height:123px;background:linear-gradient(135deg,#d9c9a8,#e8b83a 45%,#c7423a 80%,#e9e4d8)" role="img" aria-label="Share pack of colourful chips, popcorn and chocolate snacks"></div>
  <article class="item" style="left:206px;top:189px">
    <h3 class="item-title">Feeling Peckish <span class="price">$89</span></h3>
    <p>Snack Attack? A great share pack for the whole team. Chock full of tasty sweet and savoury treats including Ranchera Chipotle and Lime Tortilla Chips, Salted Pretzels, Caramel Covered Popcorn, Benny's Handmade Double Choc Chip Bites, Handmade Chocolate Roadblock, Beer Nuts and Soft Jubes.</p>
  </article>

  <article class="item" style="left:18px;top:338px">
    <h3 class="item-title" style="margin-bottom:5px">Luxury Wine Case<br>&amp; Wine of Choice <span class="price">$35+wine</span></h3>
    <p class="choose">Choose from</p>
    <ul class="wine-list">
      <li>Riverbend Sauvignon Blanc<span class="dots"></span>+$25</li>
      <li>Tallowood Pinot Noir<span class="dots"></span>+$25</li>
      <li>Kestrel Rose<span class="dots"></span>+$30</li>
      <li>Hollow Ridge Cabernet Merlot<span class="dots"></span>+$40</li>
      <li>Saltbush Point Shiraz<span class="dots"></span>+$65</li>
    </ul>
    <p>A simple yet sophisticated corporate gift. Choose from 5 different wines, presented in a mock-leather wine case which includes a bottle opener/corkscrew, a pouring spout, drip-stop ring and foil cutter.</p>
  </article>
  <div class="photo" style="left:206px;top:338px;height:164px;background:linear-gradient(160deg,#f4f4f4 0%,#f0f0f0 30%,#2a2a2a 55%,#c8202a 75%,#f3f3f3 100%)" role="img" aria-label="Black leather wine case with a bottle of white wine and red ribbon">
    <svg class="ribbon"><use href="#ribbon-right"/></svg>
  </div>

  <footer class="footer">
    <span><svg><use href="#icon-phone"/></svg>1300 42 17 88</span>
    <span><svg><use href="#icon-mail"/></svg>corporate@willowbaymail.com</span>
    <span><svg><use href="#icon-web"/></svg>www.willowbaybaskets.com.au</span>
  </footer>
</section>

<!-- Under $120 -->
<section class="page page--under120">
  <h2 class="section-band">UNDER $120</h2>

  <article class="item" style="left:18px;top:54px">
    <h3 class="item-title">Indulge Her <span class="price">$89</span></h3>
    <p>A touch of indulgence so beautifully presented, making a stunning statement of thanks. Lumen Grove Frangipani Botanical candle, Velora luxury handcream and a fun Sprinklebee Christmas treat. What more can a girl want!. A gift of gratitude and thanks.</p>
  </article>
  <div class="photo" style="left:206px;top:51px;height:114px;background:linear-gradient(160deg,#f6f3f1,#e9d3c4 45%,#e7b7b9 70%,#f2ecea)" role="img" aria-label="Candle, handcream and festive treat with a red ribbon">
    <svg class="ribbon"><use href="#ribbon-right"/></svg>
  </div>

  <div class="photo" style="left:19px;top:194px;height:142px;background:linear-gradient(135deg,#e9ecef,#3a4f7a 35%,#c99a4a 55%,#c8202a 75%,#e6e8ea)" role="img" aria-label="Gourmet chocolates, caramel sauce and Christmas cookie with red ribbon">
    <svg class="ribbon ribbon--left"><use href="#ribbon-left"/></svg>
  </div>
  <article class="item" style="left:206px;top:196px">
    <h3 class="item-title">Sweet Christmas Bites <span class="price">$119</span></h3>
    <p>Enjoy the tasty treats on offer with this gourmet gift hamper! Includes our selection of Chocolates from Harlow Cocoa &amp; Pip &amp; Parlour, Salted Caramel Sauce, a touch of Festive Fare with our Gingerbread Christmas Cookie, White Choc Christmas slice, Christmas Freckle and some sparkly additions for him and her from Glimmer Lane Crystal Christmas Bon Bon's! (Contains 2 Bon Bons containing one set of; Necklace, Earrings, Tie Clip or Cufflinks)</p>
  </article>

  <article class="item" style="left:18px;top:372px">
    <h3 class="item-title">Green Thumb <span class="price">$109</span></h3>
    <p>Our best selling staff favourite is all about self care while enjoying the beautiful outdoors. Botanically inspired &amp; designed for hardworking Gardeners. Includes Botanica Leaf Co's nourishing Wild Lime &amp; Mint SPF 15+ UVA and UVB protection hand cream, their gentle Garden Ritual Hand Wash, natural scented Citronella Candle and Hand Towel.</p>
  </article>
  <div class="photo" style="left:206px;top:369px;height:139px;background:linear-gradient(150deg,#f4f4f4,#3f5a4c 40%,#c8202a 70%,#f2f2f2)" role="img" aria-label="Green botanical hand wash, hand cream, candle and towel with red ribbon">
    <svg class="ribbon"><use href="#ribbon-right"/></svg>
  </div>

  <footer class="footer">
    <span><svg><use href="#icon-phone"/></svg>1300 42 17 88</span>
    <span><svg><use href="#icon-mail"/></svg>corporate@willowbaymail.com</span>
    <span><svg><use href="#icon-web"/></svg>www.willowbaybaskets.com.au</span>
  </footer>
</section>

</body>
</html>
```